Bolvarin Incorporated

Bolvarin is a business that provides consulting, and manages and supplies trades persons in the construction and heavy industries sector. We build, do maintenance, install machinery, and can manage projects or jobs. Would like or prefer more clean, classic designs. Blacks/greys, but open to almost anything.

Target Market(s)

Industrial/Construction/Manufacturing

Industry/Entity Type

Construction Company

Contact Information for Business Card

Clean, business name on the front, possibly have the details on the back, but open to any ideas.

Logo Text

We currently do not have a slogan, open to ideas

Font styles to use
Serif
Sans Serif

Colors

Designer to choose colors to be used in the design.

Requirements
Should not have
• the oval is not my logo, was just an idea. please don't send 20 designs with the oval

```html
<!DOCTYPE html>
<html lang="en">
<head>
<meta charset="utf-8">
<title>Bolvarin Incorporated — Business Card</title>
<link href="https://fonts.googleapis.com/css2?family=Lato:wght@400;700;900&display=swap" rel="stylesheet">
<style>
  :root {
    --backdrop: #d9d9d9;
    --card-dark: #0a0a0a;
    --card-light: #f6f5f1;
    --ink-light: #f1eee6;
    --ink-dark: #111111;
    --ink-muted: #9a968c;
    --rule: #111111;
  }
  * { margin: 0; padding: 0; box-sizing: border-box; }
  html, body {
    width: 1200px;
    height: 787px;
    overflow: hidden;
    background: var(--backdrop);
    font-family: "Lato", sans-serif;
  }
  .sheet {
    width: 1200px;
    height: 787px;
    display: flex;
    align-items: center;
    justify-content: center;
    gap: 60px;
  }
  .card {
    width: 525px;
    height: 300px;
    border-radius: 18px;
    position: relative;
    box-shadow: 0 6px 18px rgba(0,0,0,0.18);
  }
  /* Front */
  .card--front {
    background: var(--card-dark);
    display: flex;
    align-items: center;
    justify-content: center;
  }
  .brand-name {
    color: var(--ink-light);
    font-weight: 700;
    font-size: 54px;
    letter-spacing: 1px;
    text-align: center;
    line-height: 1;
  }
  .brand-name .brand-sub {
    display: block;
    font-size: 14px;
    letter-spacing: 4px;
    margin-top: 10px;
    text-transform: uppercase;
  }
  /* Back */
  .card--back {
    background: var(--card-light);
    display: flex;
    align-items: center;
    padding: 0 34px 0 40px;
  }
  .back-brand {
    width: 200px;
    display: flex;
    align-items: center;
    gap: 10px;
  }
  .back-brand .mark-dot {
    width: 14px;
    height: 14px;
    border-radius: 50%;
    background: var(--ink-dark);
    flex: none;
  }
  .back-brand .brand-text {
    color: var(--ink-dark);
    font-weight: 700;
    font-size: 30px;
    line-height: 1;
  }
  .divider {
    width: 2px;
    height: 150px;
    background: var(--rule);
    margin: 0 26px 0 14px;
    flex: none;
  }
  .details { color: var(--ink-dark); font-size: 14px; line-height: 1.45; }
  .person-name { font-weight: 900; font-size: 17px; letter-spacing: 0.5px; text-transform: uppercase; }
  .person-role { margin-bottom: 8px; }
  .address { margin-bottom: 8px; }
  .contact-list { list-style: none; }
  .contact-list li { display: flex; align-items: center; gap: 8px; }
  .contact-list svg { width: 12px; height: 12px; flex: none; }
</style>
</head>
<body>
<main class="sheet">
  <section class="card card--front" aria-label="Card front">
    <div class="brand-name">Bolvarin<span class="brand-sub">Incorporated</span></div>
  </section>

  <section class="card card--back" aria-label="Card back">
    <div class="back-brand">
      <span class="mark-dot"></span>
      <span class="brand-text">Bolvarin</span>
    </div>
    <div class="divider"></div>
    <div class="details">
      <p class="person-name">Darren Holloway</p>
      <p class="person-role">President</p>
      <p class="address">1820 Foundry Lane, Westbrook<br>NC 4, United States</p>
      <ul class="contact-list">
        <li>
          <svg viewBox="0 0 24 24" aria-hidden="true"><path fill="#111" d="M6.6 10.8a15.1 15.1 0 0 0 6.6 6.6l2.2-2.2a1 1 0 0 1 1-.25 11.4 11.4 0 0 0 3.6.57 1 1 0 0 1 1 1V20a1 1 0 0 1-1 1A17 17 0 0 1 3 4a1 1 0 0 1 1-1h3.5a1 1 0 0 1 1 1c0 1.25.2 2.45.57 3.57a1 1 0 0 1-.25 1z"/></svg>
          000-000-000-000
        </li>
        <li>
          <svg viewBox="0 0 24 24" aria-hidden="true"><rect x="2" y="5" width="20" height="14" fill="#111"/><path d="M2 5l10 8 10-8" stroke="#f6f5f1" stroke-width="2" fill="none"/></svg>
          info@websitename.com
        </li>
        <li>
          <svg viewBox="0 0 24 24" aria-hidden="true"><circle cx="12" cy="12" r="10" fill="#111"/><path d="M2 12h20M12 2c3 3 3 17 0 20M12 2c-3 3-3 17 0 20" stroke="#f6f5f1" stroke-width="1.5" fill="none"/></svg>
          www.websitename.com
        </li>
      </ul>
    </div>
  </section>
</main>
</body>
</html>
```